Personal Finance e-commerce website needs a simple budget design

Hello! I am starting to sell downloadable and printable budget planners, as shown in the attached file, for people to plan ahead on their personal finances. <br/><br/>I want to see a one-page design with similar columns (for example, "Expenses, Budget, and Actual"). I would also like to see the basic formula ("Net Income = Gross income - Total Expenses") somewhere on the design. Finally, I want the design to remain mostly minimalistic and simple for the average person to plan their personal monthly budgets.<br/><br/>However, other than that, the overall design, layout, and colors will be at the graphic designer's choice. If you have any questions for me, please let me know. Thank you for your time!

Industry/Entity Type

Financial Planning

Colors

Designer to choose colors to be used in the design.

Requirements
Must have
• I want to see a one-page design with similar columns (for example, "Expenses, Budget, and Actual").
• I want the design to remain mostly minimalistic and simple for the average person to plan their personal monthly budgets.
Nice to have
• I would also like to see the basic formula ("Net Income = Gross income - Total Expenses") somewhere on the design.

```html
<!DOCTYPE html>
<html lang="en">
<head>
<meta charset="utf-8">
<title>Basic Monthly Budget Planner</title>
<link href="https://fonts.googleapis.com/css2?family=Oswald:wght@300;400&family=Playfair+Display:wght@700;900&family=Montserrat:wght@500&display=swap" rel="stylesheet">
<style>
  :root{
    --red:#bf3a32;
    --green:#52b848;
    --blue:#4e6bb8;
    --purple:#a6479f;
    --ink:#4b58a6;
    --row-a:#efeeee;
    --row-b:#f6f6f6;
    --hint:#a9a9a9;
    --stage:#8a8a8a;
  }
  *{box-sizing:border-box;margin:0;padding:0}
  html,body{width:1200px;height:960px;overflow:hidden}
  body{background:var(--stage);position:relative;font-family:'Oswald',sans-serif}

  .planner{position:absolute;top:138px;width:485px;height:684px;background:#fff}
  .planner--warm{left:73px;--band-1:var(--red);--band-2:var(--green);--c-exp:var(--red);--c-bud:var(--green);--c-act:var(--blue);--c-net:var(--green);--c-gross:var(--green);--c-total:var(--red);--c-eq:var(--green);--c-minus:var(--red)}
  .planner--cool{left:633px;--band-1:var(--purple);--band-2:var(--blue);--c-exp:var(--purple);--c-bud:var(--blue);--c-act:var(--green);--c-net:var(--blue);--c-gross:var(--blue);--c-total:var(--purple);--c-eq:var(--blue);--c-minus:var(--purple)}

  .band{position:absolute;left:0;width:100%;height:12px}
  .band--top-1{top:0;background:var(--band-1)}
  .band--top-2{top:12px;background:var(--band-2)}
  .band--bot-1{top:660px;background:var(--band-1)}
  .band--bot-2{top:672px;background:var(--band-2)}

  .brand{position:absolute;left:44px;top:72px;font-family:'Montserrat',sans-serif;font-weight:500;font-size:23px;line-height:1;color:var(--ink)}

  .title{position:absolute;left:242px;top:38px;line-height:1;color:var(--ink);white-space:nowrap;font-weight:normal}
  .title__lead{font-family:'Playfair Display',serif;font-weight:900;font-size:19px}
  .title__main{font-family:'Oswald',sans-serif;font-weight:300;font-size:29px;margin-left:5px}

  .period{position:absolute;left:230px;top:77px;width:227px;height:42px;border:1.5px solid #b8b8b8;border-radius:21px;font-family:'Playfair Display',serif;font-weight:700;font-size:13px;line-height:1;color:#cfcfcf}
  .period__month{position:absolute;left:34px;top:22px}
  .period__year{position:absolute;left:159px;top:22px}
  .period__slash{position:absolute;left:111px;top:5px;width:1px;height:30px;background:#8a8a8a;transform:rotate(18deg)}

  .sheet{position:absolute;left:27px;top:138px;width:430px;display:grid;grid-template-columns:206px 108px 109px;column-gap:3px;row-gap:2px}
  .cell{height:35px;display:flex;align-items:center;justify-content:center;font-size:10px;font-weight:300;color:var(--hint);text-transform:uppercase;white-space:nowrap}
  .cell:nth-child(3n+1){border-radius:18px 0 0 18px}
  .cell:nth-child(3n){border-radius:0 18px 18px 0}
  .cell--head{height:42px;color:#fff;font-size:13px;font-weight:300}
  .cell--head:nth-child(1){border-radius:21px 0 0 21px;background:var(--c-exp)}
  .cell--head:nth-child(2){background:var(--c-bud)}
  .cell--head:nth-child(3){border-radius:0 21px 21px 0;background:var(--c-act)}
  .row-b{background:var(--row-b)}
  .row-a{background:var(--row-a)}

  .formula{position:absolute;left:27px;top:568px;width:430px;height:80px}
  .term{position:absolute;top:0;color:#fff}
  .term__label{height:42px;display:flex;align-items:center;justify-content:center;font-size:13px;font-weight:300;text-transform:uppercase}
  .term__hint{height:36px;margin-top:2px;display:flex;align-items:center;justify-content:center;background:var(--row-a);color:var(--hint);font-size:8px;font-weight:300;text-transform:uppercase;white-space:nowrap}
  .term--net{left:0;width:134px}
  .term--net .term__label{background:var(--c-net);border-radius:21px 0 0 21px}
  .term--net .term__hint{border-radius:18px 0 0 18px}
  .term--gross{left:169px;width:101px}
  .term--gross .term__label{background:var(--c-gross)}
  .term--gross .term__hint{background:#fff}
  .term--total{left:305px;width:125px}
  .term--total .term__label{background:var(--c-total);border-radius:0 21px 21px 0}
  .term--total .term__hint{border-radius:0 18px 18px 0}

  .operator{position:absolute;top:12px;width:19px;height:17px;border-radius:3px;display:flex;flex-direction:column;align-items:center;justify-content:center;gap:2px}
  .operator span{display:block;width:9px;height:2.5px;background:#fff;border-radius:1px}
  .operator--equals{left:142px;background:var(--c-eq)}
  .operator--minus{left:279px;background:var(--c-minus)}
</style>
</head>
<body>

<section class="planner planner--warm">
  <div class="band band--top-1"></div><div class="band band--top-2"></div>
  <div class="brand">Brightledger</div>
  <h1 class="title"><span class="title__lead">Basic Monthly</span><span class="title__main">BUDGET</span></h1>
  <div class="period"><span class="period__month">month</span><span class="period__slash"></span><span class="period__year">year</span></div>
  <div class="sheet">
    <div class="cell cell--head">Expenses (Category)</div><div class="cell cell--head">Budget (USD)</div><div class="cell cell--head">Actual (USD)</div>
    <div class="cell row-b">Custom Category</div><div class="cell row-b">What you plan to spend</div><div class="cell row-b">What you actually spent</div>
    <div class="cell row-a"></div><div class="cell row-a"></div><div class="cell row-a"></div>
    <div class="cell row-b"></div><div class="cell row-b"></div><div class="cell row-b"></div>
    <div class="cell row-a"></div><div class="cell row-a"></div><div class="cell row-a"></div>
    <div class="cell row-b"></div><div class="cell row-b"></div><div class="cell row-b"></div>
    <div class="cell row-a"></div><div class="cell row-a"></div><div class="cell row-a"></div>
    <div class="cell row-b"></div><div class="cell row-b"></div><div class="cell row-b"></div>
    <div class="cell row-a"></div><div class="cell row-a"></div><div class="cell row-a"></div>
    <div class="cell row-b"></div><div class="cell row-b"></div><div class="cell row-b"></div>
    <div class="cell row-a"></div><div class="cell row-a"></div><div class="cell row-a"></div>
  </div>
  <div class="formula">
    <div class="term term--net"><div class="term__label">Net Income</div><div class="term__hint">How much money you kept</div></div>
    <div class="operator operator--equals"><span></span><span></span></div>
    <div class="term term--gross"><div class="term__label">Gross Income</div><div class="term__hint">How much money you earned</div></div>
    <div class="operator operator--minus"><span></span></div>
    <div class="term term--total"><div class="term__label">Total Expenses</div><div class="term__hint">Actual expenses</div></div>
  </div>
  <div class="band band--bot-1"></div><div class="band band--bot-2"></div>
</section>

<section class="planner planner--cool">
  <div class="band band--top-1"></div><div class="band band--top-2"></div>
  <div class="brand">Brightledger</div>
  <h1 class="title"><span class="title__lead">Basic Monthly</span><span class="title__main">BUDGET</span></h1>
  <div class="period"><span class="period__month">month</span><span class="period__slash"></span><span class="period__year">year</span></div>
  <div class="sheet">
    <div class="cell cell--head">Expenses (Category)</div><div class="cell cell--head">Budget (USD)</div><div class="cell cell--head">Actual (USD)</div>
    <div class="cell row-b">Custom Category</div><div class="cell row-b">What you plan to spend</div><div class="cell row-b">What you actually spent</div>
    <div class="cell row-a"></div><div class="cell row-a"></div><div class="cell row-a"></div>
    <div class="cell row-b"></div><div class="cell row-b"></div><div class="cell row-b"></div>
    <div class="cell row-a"></div><div class="cell row-a"></div><div class="cell row-a"></div>
    <div class="cell row-b"></div><div class="cell row-b"></div><div class="cell row-b"></div>
    <div class="cell row-a"></div><div class="cell row-a"></div><div class="cell row-a"></div>
    <div class="cell row-b"></div><div class="cell row-b"></div><div class="cell row-b"></div>
    <div class="cell row-a"></div><div class="cell row-a"></div><div class="cell row-a"></div>
    <div class="cell row-b"></div><div class="cell row-b"></div><div class="cell row-b"></div>
    <div class="cell row-a"></div><div class="cell row-a"></div><div class="cell row-a"></div>
  </div>
  <div class="formula">
    <div class="term term--net"><div class="term__label">Net Income</div><div class="term__hint">How much money you kept</div></div>
    <div class="operator operator--equals"><span></span><span></span></div>
    <div class="term term--gross"><div class="term__label">Gross Income</div><div class="term__hint">How much money you earned</div></div>
    <div class="operator operator--minus"><span></span></div>
    <div class="term term--total"><div class="term__label">Total Expenses</div><div class="term__hint">Actual expenses</div></div>
  </div>
  <div class="band band--bot-1"></div><div class="band band--bot-2"></div>
</section>

</body>
</html>
```